integrative health clinic-Medical massage, acupuncture, chiropractic

we like our logo, but are open to new ideas. We need a new card design. We have added chiropractic and acupuncture that we have put under the name of the business. We are an integrative medical clinic

Target Market(s)

General public, athletes

Contact Information for Business Card

Phone 5055583927
Fax 5055583926
Hours Monday-Friday 9-6
Saturday 10-6
The 20% can be smaller on the back

Colors
3176b5
0355a3

Requirements
Must have
• Logo but am open to ideas
Nice to have
• We are an integrated medical clinic but also want to be personable. We want the card fun and inviting

```html
<!DOCTYPE html>
<html lang="en">
<head>
<meta charset="utf-8">
<title>Open Path Wellness – Business Card</title>
<link rel="stylesheet" href="https://fonts.googleapis.com/css2?family=Roboto+Condensed:wght@400&family=Arimo:wght@400;700&family=Crimson+Text:ital@1&family=Jost:ital,wght@0,300;1,500&display=swap">
<style>
  :root {
    --brand-blue: #1358a5;
    --frame-blue: #3176b5;
    --navy: #2e3a8c;
    --ink: #111111;
    --white: #ffffff;
    --faint-mark: #e6e8f2;
    --soft-mark: #93a5d6;
    --page: #ffffff;
  }
  * { margin: 0; padding: 0; box-sizing: border-box; }
  html, body {
    width: 1000px; height: 1200px; overflow: hidden;
    background: var(--page);
  }
  .canvas { position: relative; width: 1000px; height: 1200px; }

  .card { position: absolute; width: 663px; height: 429px; overflow: hidden; }
  .card--front { left: 161px; top: 124px; background: var(--white); border: 1px solid var(--frame-blue); }
  .card--back { left: 165px; top: 634px; background: var(--brand-blue); }

  .front-art { position: absolute; left: 0; top: 0; width: 663px; height: 429px; }

  .brand { position: absolute; left: 44px; top: 50px; }
  .brand__name {
    font-family: "Roboto Condensed", "Arial Narrow", sans-serif;
    font-weight: 400; font-size: 35px; letter-spacing: -1px;
    color: var(--ink); line-height: 1; white-space: nowrap;
  }
  .brand__dot {
    position: absolute; left: 20px; top: 46px;
    width: 26px; height: 26px; border-radius: 50%;
    background: var(--navy);
  }
  .brand__tagline {
    position: absolute; left: 73px; top: 42px; white-space: nowrap;
    font-family: "Crimson Text", Georgia, serif; font-style: italic;
    font-size: 18px; color: var(--ink);
  }
  .services {
    position: absolute; left: 50px; top: 136px;
    font-family: "Arimo", Arial, sans-serif; font-weight: 700;
    font-size: 18px; line-height: 24px; color: var(--ink);
  }

  .contact-list { position: absolute; left: 48px; top: 265px; list-style: none; }
  .contact-list li {
    display: flex; align-items: center; height: 34px;
    font-family: "Arimo", Arial, sans-serif; font-size: 16.5px; color: var(--white);
  }
  .contact-list svg { width: 22px; height: 20px; margin-right: 10px; flex: none; }

  .hours {
    position: absolute; right: 52px; top: 335px; text-align: right;
    font-family: "Arimo", Arial, sans-serif; font-size: 15px; line-height: 19px;
    color: var(--white);
  }

  .back-copy {
    position: absolute; left: 0; width: 645px; text-align: center; color: var(--white);
    white-space: nowrap;
  }
  .back-copy--specialty {
    top: 40px; font-family: "Arimo", Arial, sans-serif; font-size: 19px; font-weight: 400;
  }
  .back-copy--insurance {
    top: 73px; font-family: "Jost", "Futura", sans-serif; font-style: italic; font-weight: 500; font-size: 19.5px;
  }
  .back-mark { position: absolute; left: 217px; top: 115px; width: 210px; height: 180px; }
  .offer {
    position: absolute; left: 0; width: 645px; top: 338px; text-align: center;
    font-family: "Jost", "Futura", sans-serif; font-weight: 300; font-size: 28px;
    letter-spacing: 4px; color: var(--white);
  }
  .address {
    position: absolute; left: 0; width: 645px; top: 390px;
    display: flex; justify-content: center; align-items: center;
    font-family: "Arimo", Arial, sans-serif; font-size: 17px; color: var(--white);
  }
  .address svg { width: 16px; height: 20px; margin-right: 5px; }
</style>
</head>
<body>
<div class="canvas">

  <section class="card card--front">
    <svg class="front-art" viewBox="0 0 663 429" aria-hidden="true">
      <circle cx="496" cy="155" r="125" fill="var(--faint-mark)"/>
      <path d="M0,228 C120,205 280,205 360,258 C450,315 560,345 663,290 L663,429 L0,429 Z" fill="var(--brand-blue)"/>
    </svg>

    <div class="brand">
      <div class="brand__name">Open Path Wellness</div>
      <span class="brand__dot"></span>
      <div class="brand__tagline">Sports Therapy and Wellness Center</div>
    </div>
    <div class="services">Medical and Sports Massage<br>Acupuncture &amp; Chiropractic</div>

    <ul class="contact-list">
      <li>
        <svg viewBox="0 0 22 20"><rect x="1.5" y="4" width="19" height="12" fill="none" stroke="#fff" stroke-width="2"/><path d="M1.5 4 L11 11 L20.5 4 M1.5 16 L8 10 M20.5 16 L14 10" fill="none" stroke="#fff" stroke-width="1.6"/></svg>
        www.openpathwellnessnm.com
      </li>
      <li>
        <svg viewBox="0 0 22 20"><circle cx="11" cy="10" r="8" fill="none" stroke="#fff" stroke-width="1.5"/><ellipse cx="11" cy="10" rx="3.5" ry="8" fill="none" stroke="#fff" stroke-width="1.3"/><path d="M3 10 H19 M4.5 5.5 H17.5 M4.5 14.5 H17.5" stroke="#fff" stroke-width="1.2"/></svg>
        info@openpathwellnessnm.com
      </li>
      <li>
        <svg viewBox="0 0 22 20"><path d="M5 3 L8 3 L9 7 L7 8.5 C8 11 9.5 12.5 12 13.5 L13.5 11.5 L17 12.5 L17 15.5 C17 16.5 16 17 15 17 C9 16 4 11 4 4.5 C4 3.5 4.5 3 5 3 Z" fill="#fff"/><path d="M12 2.5 A7 7 0 0 1 18.5 9 M12 5.5 A4 4 0 0 1 15.5 9" fill="none" stroke="#fff" stroke-width="1.4"/></svg>
        5055583927
      </li>
      <li>
        <svg viewBox="0 0 22 20"><rect x="6" y="1.5" width="10" height="5" fill="#fff"/><rect x="2" y="7" width="18" height="7" rx="1.5" fill="#fff"/><rect x="6" y="12" width="10" height="6.5" fill="#fff" stroke="var(--brand-blue)" stroke-width="1"/></svg>
        5055583926
      </li>
    </ul>

    <div class="hours">Hours<br>Monday-Friday 9-6<br>Saturday 10-6</div>
  </section>

  <section class="card card--back">
    <p class="back-copy back-copy--specialty">Specializing in Medical, Sports Massage and Manual Therapies</p>
    <p class="back-copy back-copy--insurance">We accept some insurances, Worker, s Comp and Personal Injury.</p>
    <svg class="back-mark" viewBox="0 0 210 180" aria-hidden="true">
      <circle cx="105" cy="90" r="88" fill="var(--soft-mark)"/>
    </svg>
    <p class="offer">%20 OF FIRST VISIT</p>
    <p class="address">
      <svg viewBox="0 0 16 20"><path d="M8 1 C4 1 1.5 4 1.5 7.5 C1.5 12 8 19 8 19 C8 19 14.5 12 14.5 7.5 C14.5 4 12 1 8 1 Z" fill="#fff"/><circle cx="8" cy="7.5" r="2.6" fill="var(--brand-blue)"/></svg>
      1487 Cordova Rd, B4 Santa Fe, NM 87505
    </p>
  </section>

</div>
</body>
</html>
```